Bottle Label for Premium Gold CBD Oil

10 ml CBD-Oil bottle. The job is pretty straight forward and everything you need is prepared. However, the design part of the creative part ^^ The design of a lot of follow-up products we could do together. We thought about an exclusive / minimalist approach to Morvo. The bottle itself is delivered in a drawer box which looks much better than the cheap packages of the competition. Everything about the product is supposed to be honest and of high quality. The product is even more cost-effective than CBD-Oils. Key feature of the product is its deeply golden color. The design should be in harmony with this color. The customer pays a high price for this little bottle and has high expectations. Accordingly, the label should express itself and the product is worth every cent. Which it is by the way. If you would like to see the labels of the competition, just type in "CBD OIL" on "warenzelt.de". However, we are currently the only ones with a new filtration and the corresponding golden color. This label is going to be the base of a whole series of products. If we are happy with your label design, we will do a lot of following up designs with you. The logo design is already done and just needs to be implemented. We are looking forward to your designs. Many, many thanks in advance
Target Market(s)
Customers who want to use the absolute top CBD product on the market in order to improve their health
Colors
Designer to choose colors to be used in the design.
Requirements
Must have
- Please read the pdf-file with detailed descriptions and pictures. The costomer should always see that our product is of the highest quality. Please feel free to stick to our suggestions / ideas since I we are no designers. If you have your own cool approach, just submit it ^^
Nice to have
- We think it would be nice to have a drop out on the front of the label. We could imagine an exclusive / minimalist approach similar to Morvo

```html
<!DOCTYPE html>
<html lang="de">
<head>
<meta charset="utf-8">
<title>CBD Oil Premium Gold – Etikett</title>
<link rel="stylesheet" href="https://fonts.googleapis.com/css2?family=Cormorant+Garamond:wght@500&family=Oswald:wght@500&family=Roboto+Condensed:wght@400;700&display=swap">
<style>
  :root {
    --page: #ffffff;
    --side-grey: #8f8f8f;
    --side-grey-soft: #9a9a9a;
    --front-dark: #1e1e1e;
    --front-mid: #2a2a2a;
    --gold: #d9b15a;
    --gold-light: #eccb7e;
    --white: #f4f4f4;
    --side-text: #d2d2d2;
    --rule: #cfcfcf;
  }
  html, body {
    margin: 0;
    width: 1200px;
    height: 1200px;
    overflow: hidden;
    background: var(--page);
  }
  .label {
    position: absolute;
    left: 68px;
    top: 358px;
    width: 1064px;
    height: 485px;
    background: var(--side-grey);
    overflow: hidden;
  }
  .label__botanical {
    position: absolute;
    inset: 0;
    background: radial-gradient(ellipse at 50% 50%, var(--side-grey-soft) 0%, var(--side-grey) 70%);
  }
  .label__front {
    position: absolute;
    left: 338px;
    top: 0;
    width: 386px;
    height: 100%;
    background: var(--front-dark);
    color: var(--white);
    text-align: center;
  }
  .front__botanical {
    position: absolute;
    inset: 0;
    background: radial-gradient(ellipse at 50% 55%, var(--front-mid) 0%, var(--front-dark) 75%);
  }
  .brand {
    position: absolute;
    left: 0;
    right: 0;
    top: 64px;
    font-family: "Cormorant Garamond", serif;
    font-weight: 500;
    color: var(--white);
  }
  .brand__dot {
    width: 34px;
    height: 34px;
    margin: 0 auto 14px;
    border: 2px solid var(--white);
    border-radius: 50%;
  }
  .brand__line1 {
    display: flex;
    align-items: center;
    justify-content: center;
    gap: 10px;
    font-size: 15px;
    letter-spacing: 2.5px;
    line-height: 20px;
  }
  .brand__line1::before,
  .brand__line1::after {
    content: "";
    width: 44px;
    height: 1px;
    background: var(--rule);
  }
  .brand__line2 {
    font-size: 19px;
    letter-spacing: 1.5px;
    line-height: 22px;
  }
  .product-name {
    position: absolute;
    left: 0;
    right: 0;
    top: 200px;
    margin: 0;
    font-family: "Oswald", sans-serif;
    font-weight: 500;
    font-size: 62px;
    line-height: 72px;
    color: var(--gold);
    letter-spacing: 1px;
  }
  .product-line {
    position: absolute;
    left: 0;
    right: 0;
    top: 282px;
    font-family: "Oswald", sans-serif;
    font-weight: 500;
    font-size: 36px;
    line-height: 42px;
    color: var(--gold-light);
  }
  .product-type {
    position: absolute;
    left: 0;
    right: 0;
    top: 331px;
    font-family: "Roboto Condensed", sans-serif;
    font-weight: 700;
    font-size: 26px;
    line-height: 32px;
    letter-spacing: 0.5px;
  }
  .contents {
    position: absolute;
    left: 0;
    right: 0;
    top: 414px;
    font-family: "Roboto Condensed", sans-serif;
    font-weight: 400;
    font-size: 13px;
    line-height: 19px;
    color: var(--side-text);
  }
  .side-info {
    position: absolute;
    bottom: 40px;
    writing-mode: vertical-rl;
    transform: rotate(180deg);
    font-family: "Roboto Condensed", sans-serif;
    font-weight: 400;
    font-size: 12.5px;
    line-height: 19px;
    color: var(--side-text);
    margin: 0;
  }
  .side-info--maker { left: 124px; }
  .side-info--usage { left: 850px; }
  .side-info span { display: block; }
</style>
</head>
<body>
  <div class="label">
    <div class="label__botanical" role="img" aria-label="Feine Hanfblatt- und Blütenillustrationen in hellem Grau"></div>

    <p class="side-info side-info--maker">
      <span>Hergestellt in Deutschland</span>
      <span>Produzent: Feldkraut GmbH, Lindau</span>
      <span>Charge: 1234/2019</span>
      <span>Mind. haltbar bis: 10/2021</span>
    </p>

    <section class="label__front">
      <div class="front__botanical" role="img" aria-label="Zarte Hanfblatt-Illustrationen in Dunkelgrau"></div>
      <div class="brand">
        <div class="brand__dot"></div>
        <div class="brand__line1">GOLDFELD</div>
        <div class="brand__line2">HANFWERKSTATT</div>
      </div>
      <h1 class="product-name">CBD OIL</h1>
      <div class="product-line">PREMIUM GOLD</div>
      <div class="product-type">VOLLSPEKTUM</div>
      <div class="contents">
        10 ml · 250 Tropfen<br>· 1000 mg CBD
      </div>
    </section>

    <p class="side-info side-info--usage">
      <span>Anwendung:</span>
      <span>2 x 3 Tropfen täglich</span>
      <span>THC-Gehalt &lt; 0,05 %</span>
      <span>Vor Licht und Wärme schützen</span>
    </p>
  </div>
</body>
</html>
```